Halvern Properties Business Cards

I would like a business card that includes myself and my partner.
Includes: Logo, office #, email, website, our names, our numbers and possibly the address. I would also like the logo to be embossed and the card to be horizontal.
There is a photo of our yard signs to give you an idea of the colors of our business.

Target Market(s)

Everyone in real estate market.
We are in a rural area. Our clientele are from all socioeconomic backgrounds.

Industry/Entity Type

Real Estate Agent

Contact Information for Business Card

Company Name: Halvern Properties
Our Names, Titles & Cell #'s : Marla Halvern-Broker (555).316.4827, Tessa Halvern-Realtor (555).627.9154
Office #: (555).841.2600
Website: halvernproperties-example.com
Joint Email: halvern@halvernproperties-example.com
Office Address: 518B W. Cottonwell Ave.
Marrowfield, ND. 70999

Font styles to use
Serif

Requirements
Must have
• HORIZONTAL, Logo, Myself and my partners names, Our cell #'s, our office #, our website, our email address
Nice to have
• Embossed logo, office address, our titles.

```html
<!DOCTYPE html>
<html lang="en">
<head>
<meta charset="utf-8">
<title>Halvern Properties Business Card</title>
<link rel="stylesheet" href="https://fonts.googleapis.com/css2?family=Open+Sans:wght@400;600&display=swap">
<style>
  :root {
    --backdrop: #2b2b2d;
    --card-white: #ffffff;
    --brand-purple: #4b2466;
    --brand-purple-dark: #3d1c55;
    --text-light: #ffffff;
  }
  * { margin: 0; padding: 0; box-sizing: border-box; }
  html, body {
    width: 1200px; height: 900px; overflow: hidden;
    background: var(--backdrop);
    font-family: "Open Sans", Verdana, sans-serif;
  }
  .business-card {
    position: absolute; left: 110px; top: 165px;
    width: 980px; height: 570px;
    background: var(--card-white);
    border-radius: 28px;
    overflow: hidden;
    box-shadow: 0 18px 40px rgba(0,0,0,.45);
  }
  .brand {
    position: absolute; left: 0; right: 0; top: 62px;
    display: flex; justify-content: center; align-items: center; gap: 22px;
  }
  .brand-mark {
    width: 64px; height: 64px; border-radius: 50%;
    background: var(--brand-purple);
  }
  .brand-name {
    color: var(--brand-purple);
    font-weight: 600; font-size: 54px; letter-spacing: 1px;
  }
  .contact-band {
    position: absolute; left: 0; right: 0; top: 210px; height: 285px;
    background: var(--brand-purple);
    color: var(--text-light);
  }
  .agent { position: absolute; top: 28px; font-size: 18px; letter-spacing: 1.1px; }
  .agent-left { left: 40px; top: 80px; }
  .agent-right { right: 40px; text-align: right; }
  .agent-name { font-size: 30px; letter-spacing: 1.5px; line-height: 1.2; }
  .agent-title { font-size: 16px; vertical-align: super; }
  .contact-line {
    display: flex; align-items: center; gap: 14px;
    line-height: 1.5; margin-top: 3px;
  }
  .agent-right .contact-line { justify-content: flex-end; }
  .contact-line svg { width: 22px; height: 22px; flex: none; fill: var(--text-light); }
  .address { line-height: 1.25; }
  .website {
    position: absolute; left: 0; right: 0; bottom: 28px;
    text-align: center; color: var(--brand-purple-dark);
    font-size: 24px; letter-spacing: 4px;
  }
</style>
</head>
<body>
<svg width="0" height="0" style="position:absolute">
  <defs>
    <symbol id="icon-person" viewBox="0 0 24 24"><path d="M12 1a11 11 0 1 0 0 22 11 11 0 0 0 0-22zm0 4.5a3.6 3.6 0 1 1 0 7.2 3.6 3.6 0 0 1 0-7.2zM5.5 18.5c1.2-2.6 3.8-4 6.5-4s5.3 1.4 6.5 4a8.6 8.6 0 0 1-13 0z"/></symbol>
    <symbol id="icon-mobile" viewBox="0 0 24 24"><path d="M12 1a11 11 0 1 0 0 22 11 11 0 0 0 0-22zm0 2a9 9 0 1 1 0 18 9 9 0 0 1 0-18z"/><path d="M8.3 6.2l2 2.4-1.1 1.3c.9 1.9 2.4 3.4 4.3 4.3l1.3-1.1 2.4 2-1.3 2c-4.6-.6-8.4-4.4-9-9z"/></symbol>
    <symbol id="icon-phone" viewBox="0 0 24 24"><path d="M2 8c2-3 18-3 20 0l-.5 3h-4l-.5-2.2c-2.5-.7-5.5-.7-8 0L8.5 11h-4zM6 12h12l2 9H4zm6 2.2a2.6 2.6 0 1 0 0 5.2 2.6 2.6 0 0 0 0-5.2z"/></symbol>
    <symbol id="icon-mail" viewBox="0 0 24 24"><path d="M2 5h20v14H2zm1.6 1.6v.3L12 13l8.4-6.1v-.3zm0 2.3v8.5h16.8V8.9L12 15z"/></symbol>
    <symbol id="icon-pin" viewBox="0 0 24 24"><path d="M12 1a7 7 0 0 0-7 7c0 5.2 7 15 7 15s7-9.8 7-15a7 7 0 0 0-7-7zm0 4a3 3 0 1 1 0 6 3 3 0 0 1 0-6z"/></symbol>
  </defs>
</svg>

<main class="business-card">
  <header class="brand">
    <span class="brand-mark"></span>
    <span class="brand-name">Halvern Properties</span>
  </header>

  <section class="contact-band">
    <div class="agent agent-left">
      <div class="contact-line agent-name"><svg><use href="#icon-person"/></svg><span>Marla Halvern,<span class="agent-title">Broker</span></span></div>
      <div class="contact-line"><svg><use href="#icon-mobile"/></svg><span>(555).316.4827</span></div>
      <div class="contact-line"><svg><use href="#icon-phone"/></svg><span>(555).841.2600</span></div>
      <div class="contact-line"><svg><use href="#icon-mail"/></svg><span>halvern@halvernproperties-example.com</span></div>
      <div class="contact-line"><svg><use href="#icon-pin"/></svg><span class="address">518B W. Cottonwell Ave.<br>Marrowfield, ND. 70999</span></div>
    </div>

    <div class="agent agent-right">
      <div class="contact-line agent-name"><span>Tessa Halvern,<span class="agent-title">Realtor</span></span><svg><use href="#icon-person"/></svg></div>
      <div class="contact-line"><span>(555).627.9154</span><svg><use href="#icon-mobile"/></svg></div>
      <div class="contact-line"><span>(555).841.2600</span><svg><use href="#icon-phone"/></svg></div>
      <div class="contact-line"><span>halvern@halvernproperties-example.com</span><svg><use href="#icon-mail"/></svg></div>
      <div class="contact-line"><span class="address">518B W. Cottonwell Ave.<br>Marrowfield, ND. 70999</span><svg><use href="#icon-pin"/></svg></div>
    </div>
  </section>

  <footer class="website">www.halvernproperties-example.com</footer>
</main>
</body>
</html>
```